依頼詳細
■デザインのみになります。コーディング・設置は必要ありません。

ターゲットの方々が経営者や弁護士・医師の方々ですので、シックな雰囲気や高級感のあるテイストを希望しています。あまりごちゃごちゃしない方がいいです。そしてPC表示とスマートフォン表示は別のものを用意していただきたいと思っています。その辺りは以下のサイトを参照してください。

https://ka-gakuin.example/lp1/

ファッション系のサービスなので、デザインにも、そこそここだわりたいと思っています。指標となるデザインは以下を参照してください。このようなテイストが個人的に好みです。あくまで参考程度に。

https://www.verdalune.example/
https://www.shokumalink.example/user/landing/general01
https://shigoto-meijin.example/

それではみなさんからのご提案を楽しみにしております。どうぞ宜しくお願いいたします。※デザインのみになります。コーディングは必要ありません。
サイトURL
http://kiriharada.example/
ページ数
5ページ
希望イメージ
シンプル 複雑
単色 カラフル
暗い 明るい
日常 高級
遊び心 厳粛
未来的 伝統的
女性的 男性的
希望する色
青系、茶系、グレー系
納品ファイル
• フォトショップ形式 (.psd)
• PNG形式 (.png)
補足説明
・ホームページとスマートフォンでデザインが最適化されることを望んでいます。
・原稿は「添付ファイル」を参照してください。
・写真素材はこちらからダウンロードをお願いします。
http://22.filebako.example/0617-x7k29d41m3p8q05r6t2w9y4z8c1v7n3b5
■LPは縦長の1ページでお願いします
■文章量は添付ファイルをご確認ください
■ページ数が5ページとなっていますが、制作は縦長の1ページでお願いします。それなりに文章量がありますので、5ページという形で表現しています。
写真素材は以下からダウンロードしてください。http://26.filebako.example/0624-h4j8l2n6p0r3t7v1x5z9b2d6f0g4k8m1q(ギガファイル便6月24日まで)
■ 選んだ理由

センスの良さが際立っていました。ファッション分野のLPなので、細部にまで満足のいくデザインに巡り会えたのはとてもありがたいことだと感じています。

■ 提案者全員のお礼・コメント

この度は優れたデサインを多数ご提案いただきまして、誠にありがとうございました。レベルが高く、選ぶのが大変でしたがとても満足のいくコンペになりました。また機会がありましたら宜しくお願いいたします。

```html
<!DOCTYPE html>
<html lang="ja">
<head>
<meta charset="utf-8">
<title>KR styling｜経営者のための専属スタイリストサービス</title>
<link rel="stylesheet" href="https://fonts.googleapis.com/css2?family=Noto+Serif+JP:wght@400;500;600;700&family=Noto+Sans+JP:wght@400;500;700&display=swap">
<style>
:root{
  --maroon:#5b1f24;
  --maroon-deep:#4a171b;
  --gold:#b39a63;
  --ink:#2e2a28;
  --muted:#6e6862;
  --paper:#ffffff;
  --mist:#f2f0ed;
  --blush:#f4e7e6;
  --line:#d9d3cc;
}
*{margin:0;padding:0;box-sizing:border-box}
html,body{width:1200px;height:2560px;overflow:hidden;background:var(--paper)}
body{font-family:"Noto Sans JP",sans-serif;color:var(--ink);position:relative}

/* header */
.topline{height:22px;background:var(--maroon);color:#fff;font-size:11px;text-align:center;line-height:22px;letter-spacing:.05em}
.brand{height:78px;display:flex;align-items:center;justify-content:center;gap:12px}
.brand-mark{width:30px;height:30px;border-radius:50%;background:var(--maroon)}
.brand-name{font-family:"Noto Serif JP",serif;font-size:26px;font-weight:500;color:var(--ink);letter-spacing:.06em}

/* hero */
.hero{position:relative;height:360px;background:linear-gradient(90deg,#e8e6e3 0%,#f6f5f3 55%,#efedea 100%)}
.hero-photo{position:absolute;left:70px;top:0;width:380px;height:360px;background:linear-gradient(180deg,#cfcac4,#8d8680)}
.hero-copy{position:absolute;left:560px;top:60px;text-align:center;width:480px}
.hero-copy h1{font-family:"Noto Serif JP",serif;font-weight:500;font-size:34px;line-height:1.6;color:var(--ink);letter-spacing:.06em}
.hero-cta{position:absolute;left:560px;top:250px;display:flex;align-items:center;gap:14px}
.badge{width:78px;height:78px;border-radius:50%;background:var(--maroon);color:#fff;font-family:"Noto Serif JP",serif;font-size:13px;line-height:1.35;display:flex;align-items:center;justify-content:center;text-align:center}
.cta-btn{background:var(--maroon);color:#fff;width:300px;height:64px;border:1px solid var(--gold);outline:3px solid var(--maroon);display:flex;flex-direction:column;align-items:center;justify-content:center;font-family:"Noto Serif JP",serif}
.cta-btn b{font-size:22px;font-weight:500;letter-spacing:.08em}
.cta-btn small{font-size:12px;letter-spacing:.1em}

/* profile strip */
.profile{height:140px;display:flex;align-items:center;padding:0 90px;gap:30px;background:var(--paper);border-bottom:1px solid var(--line)}
.books{display:flex;gap:10px}
.book{width:62px;height:86px;background:linear-gradient(180deg,#2b3a55,#1d2638)}
.book:nth-child(2){background:linear-gradient(180deg,#e6e1d6,#bdb4a3)}
.book:nth-child(3){background:linear-gradient(180deg,#3c5a78,#22384f)}
.book:nth-child(4){background:linear-gradient(180deg,#d9d5cf,#9b948b)}
.profile-text{flex:1;text-align:center}
.profile-text p{font-family:"Noto Serif JP",serif;font-size:14px;color:var(--muted);line-height:1.6}
.profile-text h2{font-family:"Noto Serif JP",serif;font-size:30px;font-weight:600;letter-spacing:.1em}
.profile-text h2 span{font-size:14px;font-weight:400;margin-right:10px;letter-spacing:0}
.portrait{width:96px;height:96px;border-radius:50%;background:linear-gradient(180deg,#cbb9a6,#7d6a58)}

/* nav */
.nav{height:40px;display:flex;align-items:center;padding:0 40px;border-bottom:1px solid var(--line);font-size:12px}
.nav a{flex:1;text-align:center;color:var(--ink);text-decoration:none;border-right:1px solid var(--line)}
.nav a:first-child{border-left:1px solid var(--line)}
.nav .nav-cta{flex:0 0 150px;background:var(--maroon);color:#fff;height:28px;line-height:28px;margin-left:10px;border:none}

/* worries */
.worries{background:var(--mist);height:420px;padding-top:40px;position:relative}
.sec-title{font-family:"Noto Serif JP",serif;font-weight:500;font-size:25px;text-align:center;letter-spacing:.08em;white-space:nowrap}
.worries .sec-title{display:block;width:660px;margin:0 auto;padding-bottom:12px;border-bottom:1px solid var(--ink)}
.grid{display:grid;grid-template-columns:repeat(4,1fr);gap:22px 34px;width:920px;margin:30px auto 0}
.card{background:var(--blush);height:88px;display:flex;align-items:center;justify-content:center;text-align:center;font-family:"Noto Serif JP",serif;font-size:14px;line-height:1.6;border:1px solid #ead5d3}
.note{text-align:center;font-size:12px;color:var(--muted);margin-top:26px}

/* reason banner */
.reason-band{background:var(--maroon);height:70px;display:flex;align-items:center;justify-content:center;position:relative}
.reason-band h2{color:#fff;font-family:"Noto Serif JP",serif;font-weight:500;font-size:22px;letter-spacing:.08em}
.reason-band svg{position:absolute;left:580px;bottom:-18px}

/* reason body */
.reason{position:relative;height:740px;background:var(--paper)}
.figure-left{position:absolute;left:60px;top:100px;width:180px;height:480px;background:linear-gradient(180deg,#e7e4e0,#b7b1aa)}
.figure-right{position:absolute;left:990px;top:100px;width:160px;height:220px;background:linear-gradient(180deg,#efe9e0,#c9bfb2)}
.reason-text{position:absolute;left:290px;top:60px;width:660px;font-size:13px;line-height:1.9;color:var(--ink)}
.reason-text h3{font-family:"Noto Serif JP",serif;font-size:17px;font-weight:600;margin:26px 0 8px;padding-bottom:6px;border-bottom:1px solid var(--line)}
.reason-text p{margin-bottom:6px}
.reason-text em{font-style:normal;background:linear-gradient(transparent 60%,#ecdede 60%)}

/* mid cta */
.mid-cta{position:absolute;left:300px;top:620px;width:600px;height:80px;display:flex;border:1px solid var(--maroon)}
.mid-cta .tag{width:140px;background:var(--maroon);color:#fff;font-family:"Noto Serif JP",serif;font-size:16px;display:flex;align-items:center;justify-content:center;text-align:center;line-height:1.4}
.mid-cta .label{flex:1;display:flex;flex-direction:column;align-items:center;justify-content:center;font-family:"Noto Serif JP",serif;color:var(--maroon)}
.mid-cta .label b{font-size:26px;font-weight:500;letter-spacing:.1em}
.mid-cta .label small{font-size:12px;letter-spacing:.1em}

/* stylist */
.stylist{position:relative;height:690px;background:var(--maroon-deep)}
.stylist-photo{position:absolute;left:520px;top:0;width:680px;height:690px;background:linear-gradient(120deg,#6a5446,#3b2c25 60%,#2a201c)}
.stylist-head{position:absolute;left:80px;top:70px;color:#fff;font-family:"Noto Serif JP",serif;font-weight:500;font-size:36px;line-height:1.6;letter-spacing:.06em}
.stylist-box{position:absolute;left:60px;top:310px;width:440px;height:330px;background:var(--paper);padding:28px 30px}
.stylist-box h3{font-family:"Noto Serif JP",serif;font-size:17px;font-weight:600;line-height:1.6;border-bottom:1px solid var(--line);padding-bottom:12px;margin-bottom:14px}
.stylist-box p{font-size:12.5px;line-height:1.9;color:var(--ink)}
</style>
</head>
<body>

<header>
  <div class="topline">延べ2000名以上がセンスの良い経営者に変わった経営者のための専属スタイリストサービス</div>
  <div class="brand"><span class="brand-mark"></span><span class="brand-name">KR styling</span></div>
</header>

<section class="hero">
  <div class="hero-photo" role="img" aria-label="スーツ姿でバッグを持つ経営者の写真"></div>
  <div class="hero-copy"><h1>ファッションで<br>ブランディングを<br>加速させる方法とは？</h1></div>
  <div class="hero-cta">
    <div class="badge">毎月3名様<br>限定</div>
    <div class="cta-btn"><b>初回カウンセリング</b><small>お申込み受付中</small></div>
  </div>
</section>

<section class="profile">
  <div class="books" role="img" aria-label="著書の表紙が並ぶ写真">
    <div class="book"></div><div class="book"></div><div class="book"></div><div class="book"></div>
  </div>
  <div class="profile-text">
    <p>書籍3万部以上の著書を持つスタイリスト</p>
    <p>ファッションコンサルタントとして著名人・経営者を多数担当</p>
    <h2><span>スタイリスト</span>霧島 颯</h2>
  </div>
  <div class="portrait" role="img" aria-label="スタイリストの顔写真"></div>
</section>

<nav class="nav">
  <a>トップ</a><a>特徴</a><a>お客様の声</a><a>サービス内容</a><a>ご利用までの流れ</a><a>よくある質問</a>
  <a class="nav-cta">お申込みはこちら</a>
</nav>

<section class="worries">
  <h2 class="sec-title">日々のファッションにこんな悩みはありませんか？</h2>
  <div class="grid">
    <div class="card">ビジネスでの<br>ブランディングに<br>役立てたい</div>
    <div class="card">講演やセミナーなど<br>人前に立つ機会が<br>増えてきた</div>
    <div class="card">メディアに出演<br>する機会が増えた</div>
    <div class="card">今の立場にふさわしい<br>ファッションを<br>身につけたい</div>
    <div class="card">信頼される見た目に<br>変わりたい</div>
    <div class="card">自分のセンスに<br>自信がない</div>
    <div class="card">服選びが<br>面倒で時間がかかる</div>
    <div class="card">いつまでも若々しい<br>印象でいたい</div>
  </div>
  <p class="note">1つでも当てはまる方は日々のファッションを見直してみてください。</p>
</section>

<section class="reason-band">
  <h2>優秀な経営者がファッションに気を配る理由とは？</h2>
  <svg width="40" height="18" viewBox="0 0 40 18"><polygon points="0,0 40,0 20,18" fill="#5b1f24"/></svg>
</section>

<section class="reason">
  <div class="figure-left" role="img" aria-label="スーツ姿の男性のイラスト"></div>
  <div class="figure-right" role="img" aria-label="悩む男性のイラスト"></div>
  <div class="reason-text">
    <p>近年、ファッションの見た目が重要視されるようになっています。人は第一印象の数秒で相手を判断するといわれ、<em>服装はその人の信頼感を左右する</em>大切な要素です。</p>
    <p>特に経営者は、社員や取引先、メディアなど多くの人から見られる立場にあります。見た目の印象がそのまま会社の印象につながるのです。</p>
    <h3>優れた経営者ほどパーソナルブランディングを意識している</h3>
    <p>成功している経営者の多くは、自分の見せ方を戦略的に考えています。服装を整えることで<em>言葉よりも先に価値が伝わる</em>からです。</p>
    <p>一方で、忙しい日々の中で服を選ぶ時間を取るのは簡単ではありません。だからこそ、プロの力を借りて効率よく整えることが大切です。</p>
    <h3>第一印象で「センスのない服装者」にならない方法とは？</h3>
    <p>体型や年齢、立場に合わない服を選んでしまうと、どれほど高価な服でも印象は下がってしまいます。大切なのは<em>自分に合った一着を知ること</em>です。</p>
    <p>専属スタイリストが一人ひとりに合わせて提案することで、無理なく自然に、信頼される装いを手に入れることができます。</p>
  </div>
  <div class="mid-cta">
    <div class="tag">毎月3名様<br>限定</div>
    <div class="label"><b>初回カウンセリング</b><small>お申込み受付中</small></div>
  </div>
</section>

<section class="stylist">
  <div class="stylist-photo" role="img" aria-label="書斎に立つスーツ姿のスタイリストの写真"></div>
  <h2 class="stylist-head">霧島 颯、本人が<br>専属スタイリストとして<br>お手伝いします。</h2>
  <div class="stylist-box">
    <h3>300人以上の経営者のブランディングを<br>手掛けたファッションのプロ</h3>
    <p>はじめまして、スタイリストの霧島颯です。これまで300人以上の経営者や専門職の方々のファッションを担当してきました。</p>
    <p>服装は、あなたの価値を伝える最も身近な手段です。ご本人の魅力と立場にふさわしい装いを、一緒に見つけていきましょう。</p>
    <p>買い物への同行からコーディネートの提案まで、忙しい方でも無理なく続けられる形でサポートいたします。</p>
  </div>
</section>

</body>
</html>
```